Popular local dental office to begin mailing quarterly newsletters to patients

Our goal is to create an engaging and informative 4-page quarterly newsletter for our patients. This newsletter will convey our mission, strengthen doctor-patient relationships, and keep patients informed about the latest industry developments.

The newsletter needs to be print and mail-ready, utilizing our branding guidelines. While copy and photos will be provided, the design should prioritize readership and engagement. An "Morning Harbor" newsletter is provided as an example of our logo and branding, but we are looking for a fresh design that can be adapted for future issues.

Content details and an outline will be provided in a Google Doc and PDF format, which will be updated quarterly. We have also uploaded three older sample newsletters to provide a general feel, though two of them do not have the correct design. Logos are available in various formats.

The final design should accommodate different seasonal themes to keep the newsletter fresh and engaging, ultimately evoking a happy, warm, and fuzzy feeling about our dental office. We are interested in continuing with the same designer for all future quarterly newsletters. We want a design that helps our patients feel like they have chosen the best dental office ever!

Target Market(s)

Women age 35-50

Industry/Entity Type

General Dentistry Family Practice

Requirements
Nice to have
• Clean, easy to follow, easy to read with a lot of pictures

```html
<!DOCTYPE html>
<html lang="en">
<head>
<meta charset="utf-8">
<title>Cedar Ridge News – Quarterly Newsletter</title>
<link href="https://fonts.googleapis.com/css2?family=Roboto:wght@400;500&family=Roboto+Condensed:wght@500;700&display=swap" rel="stylesheet">
<style>
  :root{
    --teal:#1f4d5d;
    --orange:#e8773e;
    --amber:#f0a02c;
    --yellow:#f5b51b;
    --paper:#ffffff;
    --canvas:#f0f0f0;
    --ink:#2b2b2b;
    --muted:#666;
  }
  *{box-sizing:border-box;margin:0;padding:0}
  html,body{width:1200px;height:563px;overflow:hidden;background:var(--canvas)}
  body{font-family:"Roboto",sans-serif;color:var(--ink);position:relative}
  .page{position:absolute;top:21px;width:368px;height:504px;overflow:hidden}
  .page--cover{left:23px;background:var(--teal)}
  .page--inside{left:407px;background:var(--paper)}
  .page--back{left:800px;background:var(--teal)}
  .backdrop{position:absolute;left:0;width:100%}
  .page--cover .backdrop{top:44px;height:250px;background:linear-gradient(180deg,var(--orange) 0%,var(--amber) 58%,var(--teal) 100%)}
  .page--back .backdrop{top:0;height:285px;background:linear-gradient(180deg,var(--orange) 0%,var(--amber) 60%,var(--teal) 100%)}
  h2,.headline{font-family:"Roboto Condensed",sans-serif;font-weight:700}
  .photo{position:absolute}
  .photo--round{border-radius:50%;overflow:hidden}
  .photo--round::after{content:"";position:absolute;inset:6px;border:1px solid var(--yellow);border-radius:50%}

  /* cover */
  .masthead{position:absolute;top:0;left:0;width:100%;height:44px;background:var(--paper);display:flex;align-items:center;padding:0 22px}
  .brand{display:flex;align-items:center;gap:6px;font-family:"Roboto Condensed",sans-serif;font-weight:700;font-size:10px;line-height:1.05;color:var(--teal);text-transform:uppercase}
  .brand__dot{width:14px;height:14px;border-radius:50%;background:var(--orange)}
  .masthead__title{margin-left:auto;font-size:11.5px;font-family:"Roboto Condensed",sans-serif;font-weight:500;color:var(--orange)}
  .masthead__title b{color:var(--teal);font-weight:700}
  .doctor{position:absolute;left:188px;top:96px;color:#fff}
  .doctor .headline{font-size:22px;letter-spacing:.2px}
  .doctor p{font-size:13px;line-height:18px;margin-top:2px}
  .office-news{position:absolute;top:279px;left:0;width:100%;text-align:center;color:#fff}
  .office-news h2{font-size:14px}
  .office-news p{font-size:8px;line-height:11px;margin-top:6px}
  .trends{position:absolute;left:23px;top:363px;width:155px;color:#fff}
  .trends h2{font-size:14px}
  .trends p{font-size:8px;line-height:11px;margin-top:6px;text-align:justify}

  /* inside */
  .section-title{color:var(--teal);text-align:center;font-size:14px}
  .appreciation{position:absolute;top:25px;left:28px;right:28px;text-align:center}
  .appreciation p{font-size:8px;line-height:12.5px;margin-top:8px}
  .gallery .photo{width:142px;height:124px;border-radius:14px}
  .insights{position:absolute;top:419px;left:22px;right:22px;text-align:center}
  .insights p{font-size:8px;line-height:12.5px;color:var(--muted);margin-top:6px}

  /* back */
  .achievements{position:absolute;top:24px;left:20px;right:20px;text-align:center;color:#fff}
  .achievements h2{font-size:14px}
  .achievements p{font-size:8px;line-height:12.5px;margin-top:6px}
  .congrats{position:absolute;left:23px;top:102px;width:155px;color:#fff}
  .congrats h2{font-size:14px}
  .congrats p{font-size:8px;line-height:11px;margin-top:8px;text-align:justify;font-weight:400}
  .poster{position:absolute;left:203px;top:74px;width:137px;height:171px;background:#fff;border-radius:3px;padding:3px}
  .poster__inner{border:1.5px solid var(--orange);border-radius:3px;height:100%;padding:6px 6px;text-align:center}
  .poster__name{font-family:"Roboto Condensed",sans-serif;font-weight:700;font-size:10px;line-height:10px;color:var(--teal);text-transform:uppercase;margin-top:8px}
  .poster__tag{font-size:3.5px;font-weight:500;color:var(--teal);letter-spacing:.2px;text-transform:uppercase;margin-top:2px}
  .poster__intro{font-size:3.6px;color:var(--teal);margin-top:4px;line-height:4.6px}
  .pillar{display:flex;gap:5px;text-align:left;margin-top:5px;align-items:flex-start}
  .pillar__icon{flex:0 0 22px;height:18px;border-radius:4px;background:#f6d7c4}
  .pillar h3{font-family:"Roboto Condensed",sans-serif;font-size:5px;color:var(--teal);text-transform:uppercase}
  .pillar p{font-size:3.5px;line-height:4.4px;color:#333}
  .santa-frame{position:absolute;left:23px;top:277px;width:137px;height:173px;background:#fff;border-radius:3px;padding:3px}
  .santa-frame .photo{position:static;width:100%;height:100%;border:1.5px solid var(--orange);border-radius:3px;background:linear-gradient(135deg,#d9c9b8 0%,#c9252c 55%,#a81c22 100%)}
  .calendar{position:absolute;left:186px;top:312px;width:170px;color:#fff}
  .calendar h2{font-size:14px;line-height:16px}
  .calendar p{font-size:8px;line-height:13.8px;margin-top:9px}
  .footer{position:absolute;left:0;bottom:0;width:100%;height:23px;background:var(--orange);color:#fff;font-size:7px;display:flex;align-items:center;justify-content:center}
</style>
</head>
<body>

<!-- Page 1: cover -->
<section class="page page--cover">
  <div class="backdrop" role="img" aria-label="Sunset mountain illustration behind the cover header"></div>
  <header class="masthead">
    <div class="brand"><span class="brand__dot"></span><span>Cedar Ridge Family<br>Dentistry</span></div>
    <div class="masthead__title">Word of Mouth - <b>Cedar Ridge News</b></div>
  </header>
  <div class="photo photo--round" style="left:23px;top:62px;width:148px;height:148px;background:radial-gradient(circle at 45% 45%,#c89a7a,#6a4a8a)" role="img" aria-label="Photo of the doctor and his wife wearing leis"></div>
  <div class="doctor">
    <div class="headline">DR LAWSON</div>
    <p>Dr’s Hygienists specialists<br>financial specialists</p>
  </div>
  <div class="office-news">
    <h2>Office News</h2>
    <p>Our Commitment to Patients poster may be included in<br>this one or reference to it.</p>
  </div>
  <div class="trends">
    <h2>Industry Trends</h2>
    <p>Small, family-owned dental practices continue to be acquired by large private equity firms and corporations, mirroring a trend seen in the medical industry decades ago. As a privately-owned local small business, we are grateful for your continued support and for the opportunity to serve you. Graphic needed here.</p>
  </div>
  <div class="photo photo--round" style="left:198px;top:344px;width:148px;height:148px;background:radial-gradient(circle at 60% 55%,#e8703a,#9a8f86 70%)" role="img" aria-label="Photo of a smiling family at a community event"></div>
</section>

<!-- Page 2: inside -->
<section class="page page--inside">
  <div class="appreciation">
    <h2 class="section-title">Appreciation</h2>
    <p>Each year, Cedar Ridge Family Dentistry hosts a special Patient Appreciation Event – our way of saying a heartfelt ‘THANK YOU!’ for choosing us for your dental care. These events are a wonderful opportunity to connect with our patients outside of the office. Last year, we enjoyed a Luau, and this year, we tested our mini-golfing skills! We are truly grateful to serve you and hope you’ll join us at a<br>future event!</p>
  </div>
  <div class="gallery">
    <div class="photo" style="left:28px;top:146px;background:linear-gradient(160deg,#8fb1a8,#2f3a3a)" role="img" aria-label="Team photo of the office staff in luau shirts"></div>
    <div class="photo" style="left:185px;top:146px;background:linear-gradient(160deg,#b9a07a,#7a4038)" role="img" aria-label="Patients enjoying food at the outdoor event"></div>
    <div class="photo" style="left:28px;top:281px;background:linear-gradient(160deg,#c07a6a,#3a3a3a)" role="img" aria-label="Two staff members with leis by a food truck"></div>
    <div class="photo" style="left:185px;top:281px;background:linear-gradient(160deg,#9cc0d8,#3fa6a0)" role="img" aria-label="Guests gathered around a prize table outdoors"></div>
  </div>
  <div class="insights">
    <h2 class="section-title">Patient Care Insights</h2>
    <p>We greatly appreciate your patience as we continue our search for a hygienist who meets our high standards. A special thank you to Maren and Tessa, our amazing Registered Dental Hygienists, who are nationally recognized for their outstanding clinical skills and patient care. Photo of Maren and Tessa here</p>
  </div>
</section>

<!-- Page 3: back -->
<section class="page page--back">
  <div class="backdrop" role="img" aria-label="Sunset mountain illustration behind the achievements section"></div>
  <div class="achievements">
    <h2>Company Achievements</h2>
    <p>Once again, our office has been recognized by Brightline Dental’s Excellence Circle! This designation is awarded to only the top 20% of dental offices in the state.</p>
  </div>
  <div class="congrats">
    <h2>Congratulations</h2>
    <p>We are incredibly proud of the significant improvements in our patients’ dental health. Thank you for partnering with us to achieve healthy gums, teeth, and bites! Graphic</p>
  </div>
  <div class="poster">
    <div class="poster__inner">
      <div class="poster__name">Cedar Ridge Family<br>Dentistry</div>
      <div class="poster__tag">Healthier smiles, brighter futures</div>
      <div class="poster__intro">Our commitment is to deliver optimal oral care, focusing on three key pillars.</div>
      <div class="pillar"><div class="pillar__icon" role="img" aria-label="Gums icon"></div><div><h3>Healthy Gums</h3><p>Firm, pink gums protect your body and support overall wellness.</p></div></div>
      <div class="pillar"><div class="pillar__icon" role="img" aria-label="Tooth icon"></div><div><h3>Healthy Teeth</h3><p>We prevent cavities early so strong teeth last a lifetime.</p></div></div>
      <div class="pillar"><div class="pillar__icon" role="img" aria-label="Bite icon"></div><div><h3>Healthy Bites</h3><p>Balanced bites reduce strain and extend the life of teeth.</p></div></div>
    </div>
  </div>
  <div class="santa-frame">
    <div class="photo" role="img" aria-label="Photo of a child visiting Santa"></div>
  </div>
  <div class="calendar">
    <h2>Calendar Items<br>Santa is coming!</h2>
    <p>Meet Santa on December 13th! Skip the mall lines and secure your spot for a special, cozy visit with the Big Man. RSVP to ensure you’re on the nice list! Photo here</p>
  </div>
  <footer class="footer">© 2025.Company Name. All Rights Reserved.</footer>
</section>

</body>
</html>
```